Personal Motivational Quote Poster Design

I would like to create a poster with some of my favorite quotes to hang in my office. I did similar projects in 2012 and 2014. I've uploaded the winning designs so you can get a better idea of what I'm looking for. I will provide feedback on your design within 24 hours of receiving it.

The poster must contain the following quotes:

“What the pupil must learn, if he learns anything at all, is that the world will do most of the work for you, provided you cooperate with it by identifying how it really works and aligning with those realities. If we do not let the world teach us, it teaches us a lesson.” - Walter Brindley

“I tackle every big new problem by asking two questions: Who has dealt with this problem well? And what can we learn from them?” - Hal Porter

“If we can really understand the problem, the answer will come out of it, because the answer is not separate from the problem.” - Ravel Ondashanti

“Success is nothing more than a few simple disciplines, practiced every day; while failure is simply a few errors in judgment, repeated every day. It is the accumulative weight of our disciplines and our judgments that leads us to either fortune or failure.” - Ned Calve

“Inaction breeds doubt and fear. Action breeds confidence and courage.” - Rex Halloway

“What’s the one thing you can do, such that by doing it, everything else will be easier or unnecessary?” - Lyle Danvers

Requirements
Must have
• The poster will be 24" high x 36" long and printed on canvas, so the image you create needs to have a resolution of at least 2700 x 3900.
Nice to have
• I don't have an exact vision for how the poster should look, so I am totally open to you using your creativity to develop, arrange and present the content as you'd like.

That said, I would like an image (photo or posterized image) of the person being quoted along with each quote. I do not have specific images that I would like you to use, so you will need to find the images on your own.

The images don't need to be perfect... I am more interested in the poster relating the essence of the quotes and the people being quoted than I am in perfect photographic images of the people being quoted.

```html
<!DOCTYPE html>
<html lang="en">
<head>
<meta charset="utf-8">
<title>Quote Poster</title>
<link href="https://fonts.googleapis.com/css2?family=Montserrat:wght@400;500;600;700&display=swap" rel="stylesheet">
<style>
  :root {
    --backdrop: #918d93;
    --paper: #ffffff;
    --mat: #f1f1f3;
    --ink: #272730;
    --white: #ffffff;
    --photo-light: #b9b9bb;
    --photo-mid: #7a7a7c;
    --photo-dark: #3a3a3d;
    --mountain-a: #4e5d6b;
    --mountain-b: #6f7c86;
    --mountain-c: #3d4a3f;
  }
  * { margin: 0; padding: 0; box-sizing: border-box; }
  html, body { width: 1000px; height: 1200px; overflow: hidden; }
  body {
    background: var(--backdrop);
    font-family: "Montserrat", sans-serif;
    position: relative;
  }
  .poster { position: absolute; left: 127px; top: 53px; width: 748px; height: 1094px; background: var(--paper); }
  .mat { position: absolute; left: 155px; top: 82px; width: 692px; height: 1037px; background: var(--mat); }
  .block { position: absolute; }
  .photo { position: absolute; }
  .photo--light { background: linear-gradient(160deg, var(--photo-light), var(--photo-mid) 60%, var(--photo-dark)); }
  .photo--dark { background: linear-gradient(150deg, var(--photo-mid), var(--photo-dark) 65%, #222225); }
  .marker { position: absolute; width: 32px; height: 32px; background: var(--white); }
  .marker--framed { border: 1px solid #d9d9dc; }
  .bar { position: absolute; height: 4px; background: var(--white); }
  .tab { position: absolute; height: 7px; background: var(--ink); }
  .author { position: absolute; font-weight: 700; letter-spacing: 0.08em; text-transform: uppercase; }

  /* portrait cards */
  .card { background: var(--white); }
  .card__quote {
    position: absolute; left: 0; width: 100%;
    text-align: center; text-transform: uppercase;
    font-size: 9.6px; line-height: 11.5px; letter-spacing: 0.1em;
    color: var(--ink); font-weight: 400;
  }
  .card__quote b { font-weight: 700; }
  .card .author { left: 0; width: 100%; text-align: center; font-size: 8.4px; color: var(--ink); }

  /* dark split panels */
  .split__dark { position: absolute; top: 0; bottom: 0; background: var(--ink); }
  .split__white { position: absolute; top: 0; bottom: 0; background: var(--white); }
  .split__quote { position: absolute; color: var(--white); text-transform: uppercase; }
  .split .author { color: var(--white); }

  /* banner */
  .banner { background: linear-gradient(100deg, var(--mountain-a), var(--mountain-b) 55%, var(--mountain-c)); text-align: center; color: var(--white); }
  .banner__quote { position: absolute; left: 0; right: 0; top: 26px; font-size: 14.6px; line-height: 17.4px; font-weight: 700; letter-spacing: 0.12em; text-transform: uppercase; }
  .banner .author { left: 0; right: 0; top: 88px; font-size: 8px; letter-spacing: 0.12em; }
</style>
</head>
<body>
  <div class="poster"></div>
  <div class="mat"></div>

  <!-- Hal Porter card -->
  <section class="block card" style="left:183px; top:110px; width:167px; height:294px;">
    <div class="photo photo--light" style="left:0; top:0; width:167px; height:156px;" role="img" aria-label="Black and white portrait of Hal Porter smiling in a suit and glasses"></div>
    <div class="marker marker--framed" style="left:67px; top:139px;"></div>
    <p class="card__quote" style="top:180px;">I tackle every big new<br>problem by asking<br>two questions:<br>who has dealt with<br>this problem <b>well</b>?<br>what can we learn<br>from <b>them</b>?</p>
    <div class="author" style="top:274px;">Hal Porter</div>
  </section>
  <div class="tab" style="left:248px; top:400px; width:38px;"></div>

  <!-- Walter Brindley panel -->
  <section class="block split" style="left:378px; top:109px; width:441px; height:298px;">
    <div class="split__white" style="left:0; width:111px;"></div>
    <div class="split__dark" style="left:111px; right:0;"></div>
    <div class="photo photo--dark" style="left:0; top:57px; width:169px; height:185px;" role="img" aria-label="Black and white portrait of Walter Brindley outdoors among trees"></div>
    <div class="marker" style="left:153px; top:134px; width:30px; height:30px;"></div>
    <p class="split__quote" style="left:193px; top:117px; width:240px; font-size:9.2px; line-height:12px; font-weight:600; letter-spacing:0.08em;">What the pupil must learn, if he learns anything at all, is that the world will do most of the work for you, provided you cooperate with it by identifying how it really works and aligning with those realities. If we do not let the world teach us, it teaches us a lesson.</p>
    <div class="author" style="left:193px; top:256px; font-size:7.8px;">Walter Brindley</div>
    <div class="bar" style="left:331px; top:260px; width:85px;"></div>
  </section>

  <!-- Lyle Danvers banner -->
  <section class="block banner" style="left:183px; top:436px; width:636px; height:117px;" role="img" aria-label="Misty mountain slope with pine trees behind a quote by Lyle Danvers">
    <p class="banner__quote">What’s the one thing you can do,<br>such that by doing it, everything else<br>will be easier or unnecessary?</p>
    <div class="author">- Lyle Danvers -</div>
  </section>

  <!-- Rex Halloway panel -->
  <section class="block split" style="left:183px; top:581px; width:636px; height:172px;">
    <div class="split__white" style="left:0; width:125px;"></div>
    <div class="split__dark" style="left:125px; right:0;"></div>
    <div class="photo photo--dark" style="left:50px; top:32px; width:108px; height:108px;" role="img" aria-label="Black and white portrait of Rex Halloway resting his head on his hand"></div>
    <p class="split__quote" style="left:178px; top:28px; font-size:12.4px; font-weight:600; letter-spacing:0.08em;">Inaction breeds doubt and fear.</p>
    <p class="split__quote" style="left:178px; top:45px; font-size:18px; line-height:22.8px; font-weight:700; letter-spacing:0.1em;">Action breeds<br>confidence and<br>courage</p>
    <div class="author" style="left:178px; top:127px; font-size:10px;">Rex Halloway</div>
    <div class="bar" style="left:362px; top:131px; width:121px;"></div>
  </section>

  <!-- Ned Calve panel -->
  <section class="block split" style="left:182px; top:781px; width:449px; height:310px;">
    <div class="split__dark" style="left:0; width:289px;"></div>
    <div class="split__white" style="left:289px; right:0;"></div>
    <div class="photo photo--dark" style="left:289px; top:60px; width:160px; height:190px;" role="img" aria-label="Black and white portrait of Ned Calve seated in a suit with hands folded"></div>
    <div class="marker" style="left:273px; top:74px;"></div>
    <p class="split__quote" style="left:21px; top:151px; width:250px; font-size:8.5px; line-height:14.4px; font-weight:500; letter-spacing:0.03em;">Success is nothing more than a few simple disciplines, practiced every day; while failure is simply a few errors in judgment, repeated every day. It is the accumulative weight of our disciplines and our judgments that leads us to either fortune or failure.</p>
    <div class="author" style="left:21px; top:267px; font-size:7.8px;">Ned Calve</div>
    <div class="bar" style="left:168px; top:270px; width:92px;"></div>
  </section>

  <!-- Ravel Ondashanti card -->
  <section class="block card" style="left:659px; top:781px; width:160px; height:308px;">
    <div class="photo photo--light" style="left:0; top:0; width:160px; height:156px;" role="img" aria-label="Black and white profile portrait of Ravel Ondashanti with clasped hands"></div>
    <div class="marker marker--framed" style="left:65px; top:137px;"></div>
    <p class="card__quote" style="top:180px;">If we can really<br><b>understand</b> the<br>problem, the<br><b>answer</b> will come<br>out of it, because<br>the answer is not<br>separate from the<br>problem.</p>
    <div class="author" style="top:289px;">Ravel Ondashanti</div>
  </section>
  <div class="tab" style="left:721px; top:1084px; width:37px;"></div>
</body>
</html>
```